Logo design and Businesscard and letterhead for Technology Company

We need logo design for a new company based in Atlanta called "Vornimel". We provide information about technology Product and service provider companies, information about their Products and services. Our initial focus is to List various companies and their products, various consulting companies and their services. We want to convey the message that this will be one stop shop to find out all the information to make smart technology decisions

I am looking for Logo, Business Card and Letterhead.

Target Market(s)

Companies that have IT department, IT users such as Developers, Managers, C level, Technology Product companies , Consulting companies and service providers.

Industry/Entity Type

It Company

Requirements
Must have
• Looking for some Unique design idea.
Nice to have
• I want something that connects information across technologies between technology buyers and sellers.
Should not have
• No puzzle design.

```html
<!DOCTYPE html>
<html lang="en">
<head>
<meta charset="utf-8">
<title>Vornimel — Logo, Letterhead and Business Card</title>
<link href="https://fonts.googleapis.com/css2?family=Arimo:wght@400;700&display=swap" rel="stylesheet">
<style>
  :root {
    --ink-grey: #58595b;
    --text-grey: #4d4d4f;
    --brand-blue: #1ea9e6;
    --card-blue: #1e9ad6;
    --card-black: #05090b;
    --paper: #ffffff;
  }
  * { margin: 0; padding: 0; box-sizing: border-box; }
  html, body { width: 848px; height: 1200px; overflow: hidden; background: var(--paper); }
  body { font-family: "Arimo", Arial, sans-serif; color: var(--text-grey); position: relative; }

  .wordmark { position: absolute; display: flex; align-items: center; font-weight: 700; color: var(--ink-grey); letter-spacing: -0.02em; line-height: 1; }
  .wordmark .dot { border-radius: 50%; background: var(--brand-blue); flex: none; }
  .wordmark--hero { left: 101px; top: 82px; font-size: 72px; gap: 14px; }
  .wordmark--hero .dot { width: 32px; height: 32px; }
  .wordmark--letter { left: 151px; top: 232px; font-size: 34px; gap: 7px; }
  .wordmark--letter .dot { width: 15px; height: 15px; }
  .wordmark--card { left: 51px; top: 862px; font-size: 34px; gap: 7px; color: #ffffff; }
  .wordmark--card .dot { width: 15px; height: 15px; }

  .letterhead { position: absolute; left: 106px; top: 191px; width: 649px; height: 919px; background: var(--paper); border: 1px solid #e2e2e2; box-shadow: 2px 3px 4px rgba(0,0,0,0.28); }

  .sender { position: absolute; right: 45px; top: 44px; text-align: right; font-size: 7.4px; line-height: 9.2px; color: #6d6e70; }
  .sender .company, .sender .web { font-weight: 700; letter-spacing: 0.08em; }
  .sender .sep { color: #bbbbbb; padding: 0 2px; }

  .letter-body { position: absolute; left: 46px; top: 240px; width: 562px; font-size: 11.2px; line-height: 13.2px; letter-spacing: -0.01em; color: var(--text-grey); hyphens: auto; -webkit-hyphens: auto; }
  .letter-body p { margin-bottom: 13.2px; }
  .letter-body .indent { text-indent: 39px; }
  .letter-body .plain-line { display: inline-block; text-indent: 0; }
  .letter-body .closing { margin-top: 26px; }

  .card-back { position: absolute; left: 178px; top: 896px; width: 314px; height: 159px; background: var(--card-blue); box-shadow: 1px 2px 3px rgba(0,0,0,0.25); }
  .card-front { position: absolute; left: 33px; top: 845px; width: 314px; height: 158px; background: var(--card-black); box-shadow: 1px 2px 3px rgba(0,0,0,0.3); }
  .card-details { position: absolute; left: 44px; top: 74px; padding-left: 11px; border-left: 1px solid #6d6e70; font-size: 7px; line-height: 8.6px; color: #b7b8ba; text-transform: uppercase; }
  .card-details .name { font-size: 10px; line-height: 11px; font-weight: 700; color: #ffffff; }
  .card-details .link { color: var(--brand-blue); }
  .card-details .gap { height: 6px; }
  .card-details b { color: #ffffff; }
</style>
</head>
<body>

  <div class="wordmark wordmark--hero"><span>Vornimel</span><span class="dot"></span></div>

  <section class="letterhead">
    <div class="sender">
      <div class="company">VORNIMEL PTY LTD</div>
      <div>48 HARLOW STREET, BRENNICK FALLS, OHLEN, 48215</div>
      <div>PO BOX 517204, BRENNICK FALLS, OHLEN, 48215</div>
      <div>P: 5550 2841 <span class="sep">|</span> F: 5550 6173 <span class="sep">|</span> M: 4045550182</div>
      <div class="web">VORNIMEL.COM</div>
    </div>

    <div class="letter-body">
      <p>Dear Mr Orwin,</p>
      <p class="indent">Tet luptat, vero odipsum esequis dipsum eu feumsan henit in eu faci blam, volor suscidunt do del in hendiat duis nibh ex et velismodipis amconsequisi blandip erit ulla faciliquat, quamet ver augue feum velit lummy nulla feuissis nim dolor ad tat.<br><span class="plain-line">Te tin eumsan ut irit.</span></p>
      <p class="indent">Dolor adit il do con verat. Ut loreet, con et lummy numsan ver ipsuscidunt luptat. Na feuipisi bla feu feuguero commodit volutatio odolore minci blam, velisl exerat amcorperos nisi blam, volut lore core del utat. Ut adipit vel ipisseq uipsummod modit ing ex exero corpero core venis atue dolessis doluptat, quatie eu feugiamconse dolore tionsenisl ipsum inismolortin velit adip exer ing et pratum verat autpat.</p>
      <p class="indent">Sum nit acil ipsustrud digna atin verit inis nullaore doloreet velit venisse quatio consequat ulla consequam zzriliquis aut am dolobor aliquamet accum aliquis molore mincinim nostie et, quametuer sumsandion ent nim velit etueriu sciduis dolor adit il do con verat. Ut loreet, con et lummy numsan ver ipsuscidunt luptat. Na feuipisi bla feu feuguero commodit volutatio odolore minci blam, velisl exerat amcorperos nisi blam, volut lore core del utat. Ut adipit vel ipisseq uipsummod modit ing ex exero corpero core venis atue dolessis doluptat, quatie eu feugiamconse dolore tionsenisl ipsum inismolortin velit adip exer ing et pratum verat autpat.</p>
      <p class="closing">Regards,</p>
      <p>Dale Orwin<br>Director</p>
    </div>
  </section>

  <div class="wordmark wordmark--letter"><span>Vornimel</span><span class="dot"></span></div>

  <div class="card-back"></div>

  <section class="card-front">
    <div class="card-details">
      <div class="name">DALE ORWIN</div>
      <div>DIRECTOR</div>
      <div class="link">DALE@VORNIMEL.COM</div>
      <div class="gap"></div>
      <div>48 HARLOW STREET</div>
      <div>BRENNICK FALLS, OHLEN 48215</div>
      <div><b>P</b> I 5550 2841 <b>F</b> I 5550 2849 <b>M</b> I 4045550182</div>
      <div class="link">VORNIMEL.COM</div>
    </div>
  </section>

  <div class="wordmark wordmark--card"><span>Vornimel</span><span class="dot"></span></div>

</body>
</html>
```